Coffee Shop needs a fresh new menu

Hi,
I would like a new menu to be designed for our coffee shop.
We display our menu on a television screen, so would need it in a file that would allow us to continue to do so -- I have attached a photo so that you can see our current design, and how it is displayed.

I'd like something that is easy to read, if the design could have a "hipster" feel to it -- we are located at a hospital and University.

I have attached a Word file with what we would like on the menu.

Feel free to contact me if you have any questions.

Thanks,
Liv

Just A4 size will be fine, and no need to include menu 1 and menu 2 - I just put them in as an example of what we already have -- they are our printed menu's. Thanks

Hospital

```html
<!DOCTYPE html>
<html lang="en">
<head>
<meta charset="utf-8">
<title>Ward Nine Canteen – Menu</title>
<link rel="stylesheet" href="https://fonts.googleapis.com/css2?family=Lobster&family=Arimo:wght@400;700&family=Great+Vibes&display=swap">
<style>
  :root {
    --bg-dark: #1c1c1c;
    --bg-light: #6e6e6e;
    --paper: #c8ac8c;
    --paper-light: #d9c2a6;
    --paper-dark: #a88866;
    --red: #d9141a;
    --brown: #4a2a16;
    --bean: #5a3219;
    --bean-dark: #2e170a;
    --ink: #111;
    --white: #fff;
  }
  * { box-sizing: border-box; margin: 0; padding: 0; }
  html, body { width: 1200px; height: 1030px; overflow: hidden; }
  body {
    background: radial-gradient(ellipse at 50% 45%, var(--bg-light) 0%, #3a3a3a 55%, var(--bg-dark) 100%);
    font-family: "Arimo", Arial, sans-serif;
    position: relative;
  }
  .menu {
    position: absolute; left: 105px; top: 160px;
    display: flex; gap: 0;
    box-shadow: 0 20px 40px rgba(0,0,0,.55);
  }
  .panel {
    position: relative; width: 330px; height: 740px; overflow: hidden;
    background: linear-gradient(170deg, var(--paper-light) 0%, var(--paper) 45%, var(--paper-dark) 100%);
    border-right: 1px solid rgba(0,0,0,.25);
  }
  .band {
    position: absolute; left: 0; right: 0; top: 22px; height: 34px;
    background: var(--red);
    border-top: 3px solid var(--white);
  }
  .band--top { top: 0; height: 56px; border-top: none; border-bottom: 3px solid var(--white); }
  .script-title {
    font-family: "Lobster", cursive; color: var(--red); font-size: 30px; line-height: 1.05;
    text-shadow: -1.5px -1.5px 0 var(--white), 1.5px -1.5px 0 var(--white), -1.5px 1.5px 0 var(--white), 1.5px 1.5px 0 var(--white), 2px 3px 3px rgba(0,0,0,.45);
  }
  .script-title--on-band {
    position: absolute; left: 22px; top: 28px; color: var(--white); font-size: 26px;
    text-shadow: 2px 2px 3px rgba(0,0,0,.5);
  }
  .price-list { position: absolute; list-style: none; font-size: 15px; color: var(--ink); }
  .price-list li { display: flex; justify-content: flex-end; height: 24px; align-items: center; }
  .price-list .price { width: 58px; text-align: right; }
  .price-list--light { right: 22px; top: 122px; }
  .price-list--breakfast { right: 22px; top: 395px; font-size: 14px; }
  .price-list--hot { right: 40px; top: 218px; }
  .price-list--hot .price { width: 100px; font-weight: 700; }
  .price-list--light .price, .price-list--breakfast .price { font-weight: 400; }
  .section-title--breakfast { position: absolute; left: 22px; top: 335px; font-size: 28px; }
  .section-title--hot { position: absolute; left: 0; right: 0; top: 82px; text-align: center; }
  .photo {
    position: absolute; border-radius: 4px;
  }
  .photo--beans {
    left: 0; right: 0; bottom: 0;
    background: linear-gradient(180deg, rgba(90,50,25,0) 0%, var(--bean) 35%, var(--bean-dark) 100%);
  }
  .photo--cup-small {
    left: 20px; bottom: 24px; width: 100px; height: 76px; border-radius: 50%;
    background: radial-gradient(circle at 45% 45%, #f4f1ec 0%, #ddd6cc 60%, #b8aea2 100%);
  }
  .photo--cup-large {
    left: 25px; top: 405px; width: 285px; height: 200px; border-radius: 48%;
    background: radial-gradient(ellipse at 50% 40%, #f7f5f2 0%, #e2dcd3 55%, #b7ab9c 100%);
  }
  .ornament {
    position: absolute; right: 0; top: 210px; width: 150px; height: 260px;
    background: linear-gradient(200deg, rgba(240,225,205,.45), rgba(240,225,205,0));
  }
  .brand-strip {
    position: absolute; left: 0; right: 0; top: 548px; height: 42px;
    background: var(--brown); color: var(--white);
    font-family: "Lobster", cursive; font-size: 28px; text-align: center; line-height: 42px;
  }
  .contact-card {
    position: absolute; left: 0; right: 0; top: 590px; height: 102px;
    background: var(--white); display: flex; align-items: center; padding: 0 14px; gap: 14px;
  }
  .contact-card__brand {
    display: flex; align-items: center; gap: 6px; width: 118px;
    font-family: "Lobster", cursive; color: var(--brown); font-size: 22px; line-height: 1;
  }
  .contact-card__dot { width: 12px; height: 12px; border-radius: 50%; background: var(--brown); flex: none; }
  .contact-card__details { font-size: 12.5px; font-weight: 700; color: var(--ink); line-height: 1.2; }
  .contact-card__phone {
    display: flex; align-items: center; gap: 8px; margin-bottom: 4px;
    font-family: "Lobster", cursive; font-weight: 400; font-size: 24px; color: var(--brown);
  }
  .band__url {
    position: absolute; right: 14px; top: 20px; color: var(--white);
    font-weight: 700; font-size: 15px; letter-spacing: .3px;
  }
  .cover-brand {
    position: absolute; left: 0; right: 0; top: 130px; text-align: center;
    font-family: "Lobster", cursive; color: var(--red); font-size: 50px; line-height: 1.05;
  }
  .cover-title {
    position: absolute; left: 0; right: 0; top: 585px; text-align: center;
    font-family: "Great Vibes", cursive; font-size: 100px; color: var(--brown);
    text-shadow: -2px -2px 0 var(--white), 2px -2px 0 var(--white), -2px 2px 0 var(--white), 2px 2px 0 var(--white), 3px 4px 5px rgba(0,0,0,.5);
  }
</style>
</head>
<body>
<main class="menu">

  <section class="panel panel--left">
    <div class="band"></div>
    <h2 class="script-title script-title--on-band">Something Light</h2>
    <ul class="price-list price-list--light">
      <li><span>Mixed Yoghurts</span><span class="price">$5.50</span></li>
      <li><span>Chia Pudding</span><span class="price">$5.50</span></li>
      <li><span>Fruit Salad</span><span class="price">$5.50</span></li>
      <li><span>Bircher Muesli</span><span class="price">$5.50</span></li>
      <li><span>Protein Balls</span><span class="price">$4.0</span></li>
      <li><span>Banana Bread</span><span class="price">$4.50</span></li>
      <li><span>Muffins</span><span class="price">$4.50</span></li>
      <li><span>Slices</span><span class="price">$4.0</span></li>
    </ul>
    <h2 class="script-title section-title--breakfast">Breakfast Items</h2>
    <ul class="price-list price-list--breakfast">
      <li><span>Bacon, Egg and Cheese Roll</span><span class="price">$6.0</span></li>
      <li><span>Ham and Cheese Toastie</span><span class="price">$5.0</span></li>
      <li><span>Cheese and Tomato Toastie</span><span class="price">$5.0</span></li>
      <li><span>Ham and Cheese Croissant</span><span class="price">$6.0</span></li>
      <li><span>Cheese and Tomato Croissant</span><span class="price">$5.50</span></li>
      <li><span>Plain Croissant</span><span class="price">$3.50</span></li>
      <li><span>Hash Brown</span><span class="price">$2.0</span></li>
      <li><span>2 Piece Toast</span><span class="price">$3.0</span></li>
      <li><span>2 Piece Rasin Toast</span><span class="price">$3.0</span></li>
    </ul>
    <div class="photo photo--beans" style="height:150px;" role="img" aria-label="Photo of roasted coffee beans"></div>
    <div class="photo photo--cup-small" role="img" aria-label="Photo of a small cup of black coffee on a saucer"></div>
  </section>

  <section class="panel panel--middle">
    <div class="band"></div>
    <h2 class="script-title section-title--hot">Hot Food and<br>Sandwiches</h2>
    <ul class="price-list price-list--hot">
      <li><span>Pre Made Sandwiches</span><span class="price">$6.50 - $7.50</span></li>
      <li><span>Pre Made Focaccias</span><span class="price">$8.50</span></li>
      <li><span>Wraps</span><span class="price">$7.50</span></li>
      <li><span>Vegetarian Salad</span><span class="price">$7.50</span></li>
      <li><span>Meat/Seafood Salad</span><span class="price">$9.50</span></li>
      <li><span>Hot Chips</span><span class="price">$4.50</span></li>
      <li><span>Dim Sim</span><span class="price">$1.50</span></li>
      <li><span>Potato Cake</span><span class="price">$1.50</span></li>
      <li><span>Plain Hamburger</span><span class="price">$7.50</span></li>
      <li><span>Hamburger with the lot</span><span class="price">$9.0</span></li>
      <li><span>Chicken Schnitzel Burger</span><span class="price">$8.50</span></li>
    </ul>
    <div class="brand-strip">Ward Nine Canteen</div>
    <div class="contact-card">
      <div class="contact-card__brand"><span class="contact-card__dot"></span><span>Ward Nine</span></div>
      <div class="contact-card__details">
        <div class="contact-card__phone">
          <svg width="20" height="18" viewBox="0 0 20 18" aria-hidden="true"><path d="M2 6 Q10 0 18 6 L16 8 L13 6.5 L13 5 Q10 4 7 5 L7 6.5 L4 8 Z" fill="#4a2a16"/><rect x="4" y="9" width="12" height="8" rx="1.5" fill="#4a2a16"/></svg>
          <span>555-0199-42</span>
        </div>
        <p>48 Linden Road, Eastvale</p>
        <p>Email: hello@wardnine.cafe</p>
        <p>Website: www.wardnine.cafe</p>
      </div>
    </div>
    <div class="photo photo--beans" style="height:48px;border-radius:0;" role="img" aria-label="Photo of roasted coffee beans"></div>
  </section>

  <section class="panel panel--right">
    <div class="band band--top"><span class="band__url">WWW.WARDNINE.CAFE</span></div>
    <div class="ornament" role="img" aria-label="Decorative swirl pattern"></div>
    <p class="cover-brand">Ward Nine<br>Canteen</p>
    <div class="photo photo--beans" style="height:130px;" role="img" aria-label="Photo of roasted coffee beans"></div>
    <div class="photo photo--cup-large" role="img" aria-label="Photo of a white cup of black coffee on a saucer with a spoon"></div>
    <h1 class="cover-title">Menu</h1>
  </section>

</main>
</body>
</html>
```